Broadcaster,Conference Host,Facilitator

Looking for a business card and logo to create the Grant Felber brand .. Something with a slant towards radio and conference speaking
I like the idea of classic black white or grey but open to suggestions

Target Market(s)

Corporates

Industry/Entity Type

Business

Contact Information for Business Card

Grant Felber
Email : Grant.Felber@quorvamail.co.uk
Mobile : +44 7700 382046
Twitter : @Grantfelber

Font styles to use
Serif
Decorative
Script

Requirements
Must have
• Feel classy and dynamic
Should not have
• Cartoons

```html
<!DOCTYPE html>
<html lang="en">
<head>
<meta charset="utf-8">
<title>Grant Felber – Business Card</title>
<link href="https://fonts.googleapis.com/css2?family=Open+Sans:wght@400&display=swap" rel="stylesheet">
<style>
  :root {
    --backdrop: #1d1d1d;
    --card-front: #ededed;
    --card-back: #3c3c3e;
    --ink: #2a2a2a;
    --ink-soft: #7a7a7a;
    --rule: #3a3a3a;
    --paper-white: #ffffff;
  }
  * { margin: 0; padding: 0; box-sizing: border-box; }
  html, body {
    width: 1200px;
    height: 800px;
    overflow: hidden;
    background: var(--backdrop);
  }
  .canvas {
    position: relative;
    width: 1200px;
    height: 800px;
  }
  .card {
    position: absolute;
    top: 283px;
    width: 429px;
    height: 238px;
  }
  .card--front {
    left: 110px;
    background: var(--card-front);
    color: var(--ink);
  }
  .card--back {
    left: 638px;
    background: var(--card-back);
    display: flex;
    align-items: center;
    justify-content: center;
  }
  .identity {
    position: absolute;
    right: 222px;
    top: 175px;
    text-align: right;
  }
  .identity__name {
    font-family: "Open Sans", sans-serif;
    font-weight: 400;
    font-size: 19px;
    line-height: 1;
    letter-spacing: 0.2px;
    color: var(--ink);
  }
  .identity__role {
    margin-top: 3px;
    font-family: Arial, Helvetica, sans-serif;
    font-size: 8.4px;
    line-height: 1;
    color: var(--ink-soft);
  }
  .divider {
    position: absolute;
    left: 220px;
    top: 174px;
    width: 1px;
    height: 40px;
    background: var(--rule);
  }
  .contacts {
    position: absolute;
    left: 232px;
    top: 172px;
    list-style: none;
    font-family: "Open Sans", sans-serif;
    font-size: 10.5px;
    line-height: 15px;
    color: var(--ink);
  }
  .contacts__item {
    display: flex;
    align-items: center;
    gap: 5px;
  }
  .contacts__icon {
    width: 10px;
    height: 10px;
    flex: none;
    fill: var(--ink);
  }
  .brand-name {
    font-family: "Open Sans", sans-serif;
    font-weight: 400;
    font-size: 24px;
    letter-spacing: 3px;
    color: var(--paper-white);
  }
</style>
</head>
<body>
  <main class="canvas">
    <section class="card card--front" aria-label="Business card front">
      <div class="identity">
        <h1 class="identity__name">GRANT FELBER</h1>
        <p class="identity__role">Broadcaster,Conference Host,Facilitator</p>
      </div>
      <div class="divider"></div>
      <ul class="contacts">
        <li class="contacts__item">
          <svg class="contacts__icon" viewBox="0 0 10 10" aria-hidden="true">
            <path d="M1 3.2 Q5 0.8 9 3.2 L8.2 4.6 L6.8 4 L6.6 3.1 Q5 2.6 3.4 3.1 L3.2 4 L1.8 4.6 Z"/>
            <rect x="2.6" y="5" width="4.8" height="3.6" rx="0.6"/>
          </svg>
          <span>+44 7700 382046</span>
        </li>
        <li class="contacts__item">
          <svg class="contacts__icon" viewBox="0 0 10 10" aria-hidden="true">
            <rect x="1" y="2.4" width="8" height="5.8" rx="0.4"/>
            <path d="M1.2 2.8 L5 5.6 L8.8 2.8" stroke="#ededed" stroke-width="0.8" fill="none"/>
          </svg>
          <span>Grant.Felber@quorvamail.co.uk</span>
        </li>
        <li class="contacts__item">
          <svg class="contacts__icon" viewBox="0 0 10 10" aria-hidden="true">
            <circle cx="5" cy="5" r="4"/>
          </svg>
          <span>@Grantfelber</span>
        </li>
      </ul>
    </section>
    <section class="card card--back" aria-label="Business card back">
      <span class="brand-name">GRANT FELBER</span>
    </section>
  </main>
</body>
</html>
```